Design Business Card with our Logo

We have changed our firm name from Halbrook, Penney & Ostrand, PLLC to Halbrook, Penney & Vantrell, LLP and now need to re-design our business cards. I have attached an image of our old card so that you can see the style that we like -- clean, modern, colorful and professional. We were not thrilled with the fonts that we used on the old card, so feel free to use more modern fonts. I also attached a copy of the new logo shape, which is similar to the old one; and some other card ideas that we found in the gigcrafter.com showcase that looked nice to us. Please feel free to try different colors as we are not tied down to orange or blue. Looking for fresh new ideas.

```html
<!DOCTYPE html>
<html lang="en">
<head>
<meta charset="utf-8">
<title>Halbrook Penney Vantrell – Business Card</title>
<link rel="stylesheet" href="https://fonts.googleapis.com/css2?family=Libre+Baskerville&family=Lato:wght@400;700&display=swap">
<style>
  :root {
    --bg: #eeeeee;
    --charcoal: #48484a;
    --orange: #e8960f;
    --rust: #b85c12;
    --pale: #fbe3bb;
    --ink: #3a3a3a;
    --muted: #6b6b6b;
    --white: #ffffff;
  }
  * { margin: 0; padding: 0; box-sizing: border-box; }
  html, body { width: 1200px; height: 795px; overflow: hidden; }
  body {
    background: var(--bg);
    font-family: "Lato", sans-serif;
    position: relative;
  }
  .card {
    position: absolute;
    width: 520px;
    height: 297px;
    overflow: hidden;
    box-shadow: 0 6px 18px rgba(0,0,0,0.12);
  }
  /* Front */
  .card-front { left: 50px; top: 249px; background: var(--charcoal); }
  .front-block {
    position: absolute;
    left: 0; top: 110px;
    width: 250px; height: 187px;
    background: var(--rust);
  }
  .front-rule {
    position: absolute;
    left: 300px; top: 40px;
    width: 2px; height: 120px;
    background: #2f2f30;
  }
  .front-name {
    position: absolute;
    left: 318px; top: 50px;
    font-family: "Libre Baskerville", serif;
    font-weight: 400;
    color: var(--orange);
    text-transform: uppercase;
    font-size: 19px;
    line-height: 1.15;
    letter-spacing: 0.5px;
  }
  .front-name .tagline {
    display: block;
    font-size: 9px;
    letter-spacing: 1.2px;
    margin-top: 4px;
  }
  /* Back */
  .card-back { left: 630px; top: 249px; background: var(--white); }
  .back-faint {
    position: absolute;
    left: 0; top: 220px;
    width: 90px; height: 77px;
    background: var(--pale);
  }
  .firm {
    position: absolute;
    left: 40px; top: 70px;
    display: flex; align-items: center; gap: 12px;
  }
  .firm-square { width: 42px; height: 42px; background: var(--orange); flex: none; }
  .firm-name {
    font-family: "Libre Baskerville", serif;
    color: var(--ink);
    text-transform: uppercase;
    font-size: 13px;
    line-height: 1.15;
  }
  .firm-name .tagline { display: block; font-size: 6.5px; letter-spacing: 1px; margin-top: 2px; }
  .person { position: absolute; left: 94px; top: 150px; width: 190px; }
  .person-name { color: var(--orange); font-size: 18px; font-weight: 400; letter-spacing: 0.4px; white-space: nowrap; }
  .person-role { color: var(--muted); font-size: 10px; margin-top: 3px; }
  .divider {
    position: absolute;
    left: 300px; top: 70px;
    width: 2px; height: 100px;
    background: var(--orange);
  }
  .contact {
    position: absolute;
    left: 314px; top: 74px;
    list-style: none;
    font-size: 10.5px;
    color: var(--muted);
    line-height: 18px;
  }
  .contact li { display: flex; align-items: center; gap: 7px; }
  .contact svg { width: 10px; height: 10px; fill: var(--orange); flex: none; }
  .contact .plain { padding-left: 17px; }
</style>
</head>
<body>
  <section class="card card-front" aria-label="Card front">
    <div class="front-block"></div>
    <div class="front-rule"></div>
    <h1 class="front-name">Halbrook<br>Penney<br>Vantrell<span class="tagline">Attorneys at Law</span></h1>
  </section>

  <section class="card card-back" aria-label="Card back">
    <div class="back-faint"></div>
    <div class="firm">
      <div class="firm-square"></div>
      <div class="firm-name">Halbrook<br>Penney<br>Vantrell<span class="tagline">Attorneys at Law</span></div>
    </div>
    <div class="person">
      <div class="person-name">COLIN A. PENNEY</div>
      <div class="person-role">Partner</div>
    </div>
    <div class="divider"></div>
    <ul class="contact">
      <li><svg viewBox="0 0 10 10"><path d="M2 0.5l2 2-1 1.2c.6 1.3 1.6 2.3 2.9 2.9L7 5.6l2 2-1.3 1.9C4.3 9.3.7 5.7.5 2.3z"/></svg>555.210.4400</li>
      <li><svg viewBox="0 0 10 10"><path d="M0 2h10v6H0z M0 2l5 3.5L10 2" /></svg>cpenney@hpvlegal.com</li>
      <li><svg viewBox="0 0 10 10"><circle cx="5" cy="5" r="4.5"/></svg>www.hpvlegal.com</li>
      <li><svg viewBox="0 0 10 10"><path d="M5 0a3.5 3.5 0 0 1 3.5 3.5C8.5 6 5 10 5 10S1.5 6 1.5 3.5A3.5 3.5 0 0 1 5 0z"/></svg>22 Harbor Lane East</li>
      <li class="plain">Fairport, Florida 33990</li>
    </ul>
  </section>
</body>
</html>
```